“Manarat Al Fikr – Corporate Brochure Design Project”

We need a bilingual (Arabic-English) company brochure designed for Horizon Lantern (Horizon Lantern), a UAE-based company specializing in artificial intelligence, educational solutions, and the digital transformation of knowledge.

The brochure should be 21 cm wide by 23 cm long and have a maximum of 8-10 pages, including the cover.

The brochure will introduce the company, its services, and its strategic direction to government institutions, universities, cultural organizations, and international partners.

The brochure will reflect the company's identity as embodied in our current logo and print design, with the slogan:
"Experts integrating knowledge with technology to serve humanity." The brochure text is attached.
Also attached is the company's visual identity guide and the company logo in horizontal and vertical formats.

```html
<!DOCTYPE html>
<html lang="en">
<head>
<meta charset="utf-8">
<title>Manarat Al Fikr – Brochure Spreads</title>
<link href="https://fonts.googleapis.com/css2?family=Poppins:ital,wght@0,400;0,500;0,600;0,700;1,400;1,600&family=Tajawal:wght@400;500;700;800&display=swap" rel="stylesheet">
<style>
:root{
  --backdrop:#cdc9ca;
  --paper:#ffffff;
  --navy:#1f2a6b;
  --ink:#2a2a2a;
  --blue:#0d4fc4;
  --blue-deep:#0a3a9c;
  --teal:#3fb8b3;
  --teal-light:#6fd3e0;
  --accent-red:#e0001b;
  --rule:#9cc6d0;
}
*{box-sizing:border-box;margin:0;padding:0}
html,body{width:786px;height:1200px;overflow:hidden;background:var(--backdrop)}
body{position:relative;font-family:'Poppins',sans-serif;color:var(--ink)}
.page{position:absolute;width:327px;height:358px;background:var(--paper);overflow:hidden}
.p1{left:48px;top:47px}.p2{left:408px;top:47px}
.p3{left:48px;top:426px}.p4{left:408px;top:426px}
.p5{left:48px;top:804px}.p6{left:408px;top:804px}
.ar{font-family:'Tajawal',sans-serif;direction:rtl;text-align:right}
.en{text-align:justify}

/* running header */
.brand-head{position:absolute;left:25px;top:17px;right:33px;display:flex;align-items:center;gap:6px}
.brand-head .name{font-weight:700;font-size:8.5px;color:var(--navy);white-space:nowrap}
.brand-head .rule{flex:1;height:0.6px;background:var(--rule);margin-top:1px}

/* footer */
.page-foot{position:absolute;left:25px;right:25px;bottom:17px;display:flex;align-items:center;gap:4px}
.page-foot .dot{width:13px;height:13px;border:1px solid var(--navy);border-radius:50%}
.page-foot .rule{flex:1;height:0.6px;background:var(--navy)}
.page-foot .num{width:8px;height:8px;border-radius:50%;background:var(--teal);color:#fff;font-size:4px;display:flex;align-items:center;justify-content:center;font-weight:600}

.h-ar{font-weight:800;color:var(--navy);font-size:10.5px}
.h-en{font-weight:600;color:var(--navy);font-size:9.5px}
.body-ar{font-size:6px;line-height:1.55;color:#222}
.body-en{font-size:6.4px;line-height:1.45;color:#222}
.photo{position:absolute}

/* cover */
.cover{background:linear-gradient(160deg,#2a62cc 0%,#1044b0 45%,#0b3a9e 100%)}
.cover .scene{position:absolute;inset:0;background:radial-gradient(ellipse at 35% 60%,rgba(150,190,255,.45),transparent 55%),radial-gradient(ellipse at 80% 40%,rgba(120,170,240,.35),transparent 50%)}
.cover-tag{position:absolute;top:26px;width:100%;text-align:center;color:#fff;font-size:11px;direction:rtl;font-family:'Tajawal',sans-serif}
.cover-title{position:absolute;top:46px;width:100%;text-align:center;color:#fff;font-size:27px;font-weight:500;font-family:'Tajawal',sans-serif}
.cover-mark{position:absolute;top:160px;width:100%;display:flex;flex-direction:column;align-items:center;gap:10px}
.cover-mark .badge{width:58px;height:58px;border-radius:50%;background:rgba(255,255,255,.12)}
.cover-mark .name{color:#fff;font-weight:700;font-size:15px;letter-spacing:.3px}
.cover-company{position:absolute;top:301px;width:100%;text-align:center;color:#fff;font-weight:700;font-size:12px;letter-spacing:.3px}
.cover-slogan{position:absolute;top:320px;width:100%;text-align:center;color:#fff;font-size:6.4px;letter-spacing:.2px}

/* back cover */
.back{background:linear-gradient(170deg,#1650c6 0%,#0d43b4 60%,#0b3aa2 100%)}
.back .glow{position:absolute;inset:0;background:radial-gradient(ellipse at 50% 45%,rgba(120,170,255,.35),transparent 60%)}
.back .center{position:absolute;left:0;right:0;text-align:center;color:#fff}
.back .badge{position:absolute;left:142px;top:28px;width:43px;height:43px;border-radius:50%;background:rgba(255,255,255,.14)}
.contact-list{display:flex;flex-direction:column;align-items:center;gap:3px;font-size:5.4px}
.contact-list span{display:flex;align-items:center;gap:3px}
.contact-list svg{width:5px;height:5px}
</style>
</head>
<body>

<!-- Cover -->
<section class="page p1 cover">
  <div class="scene" role="img" aria-label="Background photo of a human hand reaching toward a robotic hand over glowing blue circuitry"></div>
  <p class="cover-tag">[شعار منارة الفكر]</p>
  <h1 class="cover-title">منارة الفكر</h1>
  <div class="cover-mark">
    <div class="badge"></div>
    <div class="name">MANARAT AL FIKR</div>
  </div>
  <p class="cover-company">HORIZON LANTERN</p>
  <p class="cover-slogan">EXPERTS INTEGRATING KNOWLEDGE WITH TECHNOLOGY TO SERVE HUMANITY</p>
</section>

<!-- Page 02 -->
<section class="page p2">
  <header class="brand-head"><span class="name">Manarat Al Fikr</span><span class="rule"></span></header>
  <div class="photo" style="left:25px;top:47px;width:252px;height:82px;background:radial-gradient(circle at 55% 45%,#5fc6f0 0%,#1a6fa8 30%,#0a3150 70%,#06202f 100%)" role="img" aria-label="Photo of a hand holding a glowing globe surrounded by technology icons"></div>
  <div class="photo" style="left:284px;top:47px;width:43px;height:82px;background:var(--blue)"></div>
  <div style="position:absolute;left:25px;right:25px;top:140px">
    <h2 class="ar h-ar">عالم جديد من المعرفة ينتظرك</h2>
    <p class="ar body-ar" style="margin-top:4px">في عصر يتسارع فيه التطور التكنولوجي، لم تعد المعرفة مجرد معلومات تُقرأ، بل أصبحت تجربة حية نعيشها ونتفاعل معها. في "منارة الفكر"، نحن لا نواكب هذا التغيير فحسب، بل نصنعه.</p>
    <p class="ar body-ar" style="margin-top:4px">ندعوكم لاستكشاف كيف يمكن للذكاء الاصطناعي والواقع الغامر أن يحول أفكاركم إلى تجارب خالدة، وكيف يمكن لخبراتنا أن تفتح لكم أبواباً نحو آفاق لم تكن ممكنة من قبل. هذه ليست مجرد خدمات، بل رحلة نحو المستقبل نبدأها معكم.</p>
    <h2 class="h-en" style="margin-top:11px">A New World of Knowledge Awaits</h2>
    <p class="en body-en" style="margin-top:6px">In an era of accelerating technological advancement, knowledge is no longer just information to be read; it has become a living experience we inhabit and interact with. At Horizon Lantern, we do not just keep up with this change - we create it.</p>
    <p class="en body-en" style="margin-top:6px">We invite you to discover how Artificial Intelligence and immersive reality can transform your ideas into timeless experiences, and how our expertise can open doors to previously unimaginable horizons. These are not just services we offer; this is a journey into the future that we embark on with you.</p>
  </div>
  <footer class="page-foot"><span class="dot"></span><span class="rule"></span><span class="num">02</span></footer>
</section>

<!-- Page 03 -->
<section class="page p3">
  <header class="brand-head"><span class="name">Manarat Al Fikr</span><span class="rule"></span></header>
  <div style="position:absolute;left:25px;right:25px;top:46px">
    <h2 class="ar h-ar">كلمتنا</h2>
    <p class="ar body-ar" style="margin-top:3px">أهلاً بكم في "منارة الفكر"، حيث لا نرى المستقبل كوجهة بعيدة، بل كواقع نصنعه اليوم في عالم تقوده البيانات وتشكله التقنية، نؤمن بأن المعرفة الحقيقية هي التي تجمع بين عمق التراث ورؤية المستقبل.</p>
    <p class="ar body-ar" style="margin-top:3px">لقد أسسنا هذه الشركة على مبدأ أساسي: تحويل الإمكانيات إلى واقع ملموس. نرى في كل فكرة فرصة لابتكار تجربة فريدة، وفي كل تحد دافعاً لتطوير حلول أذكى. شراكاتنا الاستراتيجية، مثل عضويتنا في صندوق الساحل لتنمية المشاريع، وتوزيعنا لبرامج عالمية مثل حكايات المدينة، هي شهادة على التزامنا بالجودة والثقة.</p>
    <p class="ar body-ar" style="margin-top:3px">ندعوكم لتكونوا جزءاً من هذه الرحلة، لنبني معاً حلولاً معرفية تترك أثراً وتلهم الأجيال القادمة.</p>
    <h2 class="h-en" style="margin-top:9px">Our Word</h2>
    <div style="display:flex;gap:12px;margin-top:4px">
      <p class="en body-en" style="font-style:italic;width:132px">Welcome to Horizon Lantern, where we do not see the future as a distant destination, but as a reality we are building today. In a world driven by data and shaped by technology, we believe that true knowledge is what combines the depth of heritage with the vision of the future.</p>
      <div style="width:131px;height:63px;margin-top:-3px;background:radial-gradient(circle at 50% 40%,#4fb4d8 0%,#1d4f72 40%,#1a2a3a 100%)" role="img" aria-label="Photo of a person holding a glowing AI symbol above open hands"></div>
    </div>
    <p class="en body-en" style="font-style:italic;margin-top:5px">We founded this company on a fundamental principle: turning potential into tangible reality. We see in every idea an opportunity to innovate a unique experience, and in every challenge a motivation to develop smarter solutions. Our strategic partnerships, such as our membership in the Coastal Enterprise Growth Fund and our distribution of global programs like "City Stories," are a testament to our commitment to quality and trust.</p>
    <p class="en body-en" style="font-style:italic;margin-top:5px">We invite you to be part of this journey, to build together knowledge-based solutions that make an impact and inspire future generations.</p>
  </div>
  <footer class="page-foot"><span class="dot"></span><span class="rule"></span><span class="num">03</span></footer>
</section>

<!-- Page 04 -->
<section class="page p4">
  <header class="brand-head"><span class="name">Manarat Al Fikr</span><span class="rule"></span></header>
  <div style="position:absolute;left:25px;right:25px;top:45px">
    <h2 class="ar h-ar">من نحن – رواد صناعة المعرفة المستقبلية</h2>
    <p class="ar body-ar" style="margin-top:3px">منارة الفكر "ليست مجرد شركة بل هي منظومة متكاملة من الخبرات والشراكات وجدت لهدف" واحد: إعادة تعريف مستقبل المعرفة</p>
    <p class="ar body-ar" style="margin-top:4px">تأسست "منارة الفكر" بفخر كعضو في صندوق الساحل لتنمية المشاريع، وانطلقت على أيدي نخبة من الخبراء المتخصصين في مجالات المعرفة والتحول الرقمي. منذ اليوم الأول، كانت غايتنا واضحة: بناء جسر متين يربط بين تراثنا الثقافي الغني والإمكانيات المستقبلية للذكاء الاصطناعي</p>
    <p class="ar body-ar" style="margin-top:4px">سرد قصصهم بطرق لم تكن ممكنة من قبل. يملك فريقنا خبرة عميقة في نقل المعرفة من شكلها التقليدي إلى تجارب رقمية غامرة، مما يمكن شركاءنا من</p>
  </div>
  <div class="photo" style="left:0;top:149px;width:277px;height:107px;background:radial-gradient(ellipse at 55% 30%,#1f7fb8 0%,#0b2a5a 45%,#07132e 100%)" role="img" aria-label="Photo of glowing blue AI letters on a dark digital background"></div>
  <div class="photo" style="left:284px;top:150px;width:43px;height:106px;background:var(--blue)"></div>
  <div style="position:absolute;left:0;top:208px;width:277px;height:48px;background:rgba(37,47,110,.95);padding:6px 0 0 25px;color:#fff">
    <h2 style="font-size:10px;font-weight:600;white-space:nowrap">Who We Are - Pioneers of Future Knowled</h2>
    <p style="font-size:6.2px;font-style:italic;margin-top:5px;line-height:1.45;width:230px">Horizon Lantern is more than just a company; it is an integrated ecosystem of expertise and partnership</p>
  </div>
  <p class="en body-en" style="position:absolute;left:25px;right:25px;top:263px">Proudly established as a <b style="color:var(--accent-red);font-weight:600">member of the Coastal Enterprise Growth Fund in Dubai,</b> Horizon Lantern was launched by a selection of elite experts specializing in knowledge and digital transformation. From day one, our goal has been clear: to build a solid bridge connecting our rich cultural heritage with the limitless possibilities of Artificial Intelligence.</p>
  <footer class="page-foot"><span class="dot"></span><span class="rule"></span><span class="num">04</span></footer>
</section>

<!-- Page 05 -->
<section class="page p5">
  <header class="brand-head"><span class="name">Manarat Al Fikr</span><span class="rule"></span></header>
  <div style="position:absolute;left:25px;right:25px;top:46px">
    <p class="en body-en">Our team possesses deep experience in transforming traditional knowledge into immersive digital experiences, enabling our partners to tell their stories in ways never before possible.</p>
    <h2 class="ar h-ar" style="text-align:left;margin-top:6px">رؤيتنا ورسالتنا</h2>
    <div style="display:flex;gap:22px;margin-top:3px">
      <div class="ar" style="flex:1;text-align:left">
        <p style="color:var(--teal);font-size:6px">رؤيتنا:</p>
        <p class="body-ar" style="text-align:right;margin-top:3px">أن نكون الشريك الرائد عالمياً في صناعة تجارب معرفية غامرة، وأن نصبح الشريك الموثوق لكل مؤسسة تطمح إلى سرد قصتها بطريقة مبتكرة تليق بقيمتها</p>
      </div>
      <div class="ar" style="flex:1;text-align:left">
        <p style="color:var(--teal);font-size:6px">رسالتنا</p>
        <p class="body-ar" style="text-align:right;margin-top:3px">تمكين شركائنا من خلال تحويل محتواهم الثقافي والتعليمي إلى أصول رقمية تفاعلية باستخدام أحدث التقنيات مع الالتزام بأعلى معايير الدقة والجودة، والإبداع لتقديم قيمة حقيقية للمجتمع</p>
      </div>
    </div>
    <h2 class="h-en" style="margin-top:8px">Our Vision</h2>
    <p class="en body-en" style="margin-top:4px">To be the globally leading partner in creating immersive knowledge experiences, and to become the trusted partner for every organization aspiring to tell its story in an innovative way that befits its value.</p>
  </div>
  <div class="photo" style="left:0;top:204px;width:46px;height:73px;background:var(--blue)"></div>
  <div class="photo" style="left:46px;top:204px;width:167px;height:73px;background:linear-gradient(135deg,#9fb9d8 0%,#3a5f8e 45%,#13294d 100%)" role="img" aria-label="Photo of a digital globe with streams of binary data"></div>
  <div style="position:absolute;left:46px;top:262px;width:167px;height:15px;background:rgba(37,47,110,.92);color:#fff;font-weight:600;font-size:9.5px;padding:1px 0 0 7px">Our Mission</div>
  <div class="photo" style="left:219px;top:204px;width:83px;height:73px;background:radial-gradient(circle at 50% 45%,#8fc4ee 0%,#2a5fa0 45%,#0d2b5c 100%)" role="img" aria-label="Photo of a hand touching a digital data dashboard"></div>
  <div style="position:absolute;left:14px;top:277px;width:0.6px;height:14px;background:var(--navy)"></div>
  <p class="en body-en" style="position:absolute;left:26px;right:25px;top:280px">To empower our partners by transforming their cultural and educational content into interactive digital assets using the latest technologies, while adhering to the highest standards of accuracy, quality, and creativity to deliver true value to the community.</p>
  <footer class="page-foot"><span class="dot"></span><span class="rule"></span><span class="num">05</span></footer>
</section>

<!-- Back cover -->
<section class="page p6 back">
  <div class="glow" role="img" aria-label="Soft blue background with faint hexagons and circuit lines"></div>
  <div class="badge"></div>
  <div class="center" style="top:84px">
    <h2 class="ar" style="text-align:center;font-weight:700;font-size:10.5px">تواصل معنا</h2>
    <p class="ar" style="text-align:center;color:var(--teal-light);font-size:6.5px;margin-top:2px">هل أنت مستعد لبدء رحلتك نحو مستقبل المعرفة؟</p>
    <p class="ar" style="text-align:center;font-size:5.4px;margin-top:7px">تواصل معنا اليوم لترى كيف يمكننا مساعدتك</p>
    <div class="contact-list ar" style="margin-top:8px">
      <span>الهاتف: أدخل رقم الهاتف هنا</span>
      <span>البريد الإلكتروني: أدخل البريد الإلكتروني هنا</span>
      <span>الموقع الإلكتروني: أدخل الموقع الإلكتروني هنا</span>
      <span>العنوان: أدخل العنوان هنا</span>
    </div>
  </div>
  <div class="center" style="top:194px">
    <h2 style="font-weight:700;font-size:9px;line-height:1.35">Ready to start your journey into the future<br>of knowledge?</h2>
    <p style="color:var(--teal-light);font-size:8px;margin-top:9px">Contact us today to see how we can help you.</p>
    <div class="contact-list" style="margin-top:8px">
      <span><svg viewBox="0 0 10 10"><circle cx="5" cy="5" r="5" fill="#6fd3e0"/><path d="M3 3l1.2-.3.8 1.6-.7.5a4 4 0 0 0 1.9 1.9l.5-.7 1.6.8L8 8C5 8 2 5 3 3z" fill="#0d43b4"/></svg>Phone: [Enter phone number here]</span>
      <span><svg viewBox="0 0 10 10"><circle cx="5" cy="5" r="5" fill="#6fd3e0"/><rect x="2.5" y="3.2" width="5" height="3.6" fill="none" stroke="#0d43b4" stroke-width=".8"/><path d="M2.5 3.2L5 5.2l2.5-2" fill="none" stroke="#0d43b4" stroke-width=".8"/></svg>Email: [Enter email here]</span>
      <span><svg viewBox="0 0 10 10"><circle cx="5" cy="5" r="5" fill="#6fd3e0"/><circle cx="5" cy="5" r="2.6" fill="none" stroke="#0d43b4" stroke-width=".7"/><path d="M2.4 5h5.2M5 2.4v5.2" stroke="#0d43b4" stroke-width=".6"/></svg>Website: [Enter website here]</span>
      <span><svg viewBox="0 0 10 10"><circle cx="5" cy="5" r="5" fill="#6fd3e0"/><path d="M5 8L3.2 5.2a2 2 0 1 1 3.6 0z" fill="#0d43b4"/></svg>Address: [Enter address here]</span>
    </div>
  </div>
  <div style="position:absolute;left:154px;top:311px;width:19px;height:0.6px;background:#fff"></div>
  <p class="center" style="top:324px;font-size:6px">Experts integrating knowledge with technology to serve humanity</p>
</section>

</body>
</html>
```